Inspirational Quote Poster for Employees

For this project, we need a simple yet high-impact poster template that will be customized for each of our employees with a personalized inspirational quote and color scheme. This template should allow us to quickly and easily customize the text and colors in the poster without a lot of effort.

The poster design should consist of:
- A stylized text area to contain the main text of the quote
- A separate text area to contain the source of quote
- A background that complements the color and style of the text

Text may use different typographic effects (such as color, stroke weight, italicization, font size changes, drop shadows) to draw attention to words in the quote; the source of the quote may be formatted the same as the main text of the quote, or may be formatted differently to distinguish it from the main quote.

The background may be simply a single color, subtle texture, gradients, halftone effects, or other color/texture effects may be used to complement the text.

Examples of the types of posters envisioned by this project:
- http://www.pinvelora.example/marcusdtelford/quillbase-job-1/

Sample quotes to use to build your poster - choose whichever one you want, but be certain that the poster design will handle both long and short quotes:
- "Happiness in intelligent people is the rarest thing I know" - Walden Prosket
- "Wanting to be someone else is a waste of the person you are." - Rolf Dintey
- "Experience is not what happens to you. It is what you do with what happens to you." - Ferris Mundell
- "Simplicity is the ultimate in sophistication." - Rinaldo de Pavesco
- "You will get all you want in life if you help enough other people get what they want." - Tad Pomfrey
- "Hell, there are no rules here — we're trying to accomplish something." - Gareth Vullane

Industry/Entity Type

Quote

Requirements
Must have
• Final deliverable must be:
• - Formatted for an 18” x 24” poster (in portrait orientation)
• - Delivered in Adobe InDesign, Adobe Illustrator, or Extended PostScript format
• - Use CMYK color mode
• - Be print-ready at 300dpi resolution
• - Include any fonts used in the template

```html
<!DOCTYPE html>
<html lang="en">
<head>
<meta charset="utf-8">
<title>Simplicity Quote Poster</title>
<link href="https://fonts.googleapis.com/css2?family=Stint+Ultra+Condensed&display=swap" rel="stylesheet">
<style>
  :root {
    --backdrop: #cfd0d2;
    --paper: #ffffff;
    --paper-edge: #3a3a3a;
    --bubble-light: #e6e62a;
    --bubble-mid: #d8e433;
    --bubble-deep: #c6df3c;
    --ink: #363433;
  }
  * { margin: 0; padding: 0; box-sizing: border-box; }
  html, body {
    width: 1200px;
    height: 900px;
    overflow: hidden;
    background: var(--backdrop);
  }
  .stage {
    position: relative;
    width: 1200px;
    height: 900px;
  }
  .poster {
    position: absolute;
    left: 280px;
    top: 22px;
    width: 640px;
    height: 856px;
    background: var(--paper);
    border: 1px solid var(--paper-edge);
    overflow: hidden;
  }
  .speech-bubble {
    position: absolute;
    left: 0;
    top: 0;
    width: 640px;
    height: 856px;
  }
  .quote {
    position: absolute;
    left: 0;
    top: 248px;
    width: 640px;
    padding-right: 8px;
    text-align: center;
    font-family: "Stint Ultra Condensed", "Arial Narrow", serif;
    font-weight: 400;
    font-size: 90px;
    line-height: 110px;
    letter-spacing: -1px;
    color: var(--ink);
    text-transform: uppercase;
  }
  .quote-line { display: block; white-space: nowrap; }
  .quote-source {
    position: absolute;
    left: 130px;
    top: 742px;
    font-family: "Stint Ultra Condensed", "Arial Narrow", serif;
    font-size: 20px;
    letter-spacing: 0.5px;
    color: var(--ink);
    text-transform: uppercase;
    white-space: nowrap;
  }
</style>
</head>
<body>
  <main class="stage">
    <article class="poster">
      <svg class="speech-bubble" viewBox="0 0 640 856" aria-hidden="true">
        <defs>
          <linearGradient id="bubbleFill" x1="0" y1="0" x2="1" y2="1">
            <stop offset="0" stop-color="var(--bubble-light)"/>
            <stop offset="0.55" stop-color="var(--bubble-mid)"/>
            <stop offset="1" stop-color="var(--bubble-deep)"/>
          </linearGradient>
        </defs>
        <path fill="url(#bubbleFill)" d="M 250 120 C 360 110 470 125 545 150 C 610 175 635 240 625 300 C 618 350 590 390 590 430 C 600 500 620 560 590 610 C 550 660 450 670 370 660 C 300 652 240 650 218 668 C 205 685 202 705 200 725 C 193 700 180 670 150 655 C 100 630 40 610 20 540 C 0 470 10 380 40 300 C 80 200 150 130 250 120 Z"/>
      </svg>
      <blockquote class="quote">
        <span class="quote-line">Simplicity</span>
        <span class="quote-line">is the ultimate in</span>
        <span class="quote-line">sophistication.</span>
      </blockquote>
      <p class="quote-source">- Rinaldo de Pavesco</p>
    </article>
  </main>
</body>
</html>
```